Trade Show Banner "Brindlequay"

1.7' x 3' vertical banner to complement trade show booth panels (3-panel tabletop booth attached). The word file (attached) is for text and not meant to imply design. We manage homeowner and condo associations that are run by volunteer boards of directors who already have full-time jobs or who may have no training in how to run an organization. It can be highly stressful and not very rewarding. We want this poster/banner to convey that feeling of stress along with a hope for relief and relaxation. Our logo is attached. The full logo is the top one in the file. You may also want to use the triangle (attached) in addition to or instead of the logo. Our corporate fonts are attached. Please let me know if you need additional information or if you feel like there is too much copy or any other thoughts or comments you have.

Target Market(s)

Volunteer boards of directors for homeowner and condo associations--all ages, genders, races, occupations.

Industry/Entity Type

Property Management

Other font styles liked:
• "Copper Lantern" is part of a trademark and should be in Mistral with the green from our logo

Requirements
Must have
• Simple, easy to read, don't clash with booth design
Nice to have
• convey the tension of stress contrasted with the feeling of relaxation and relief.

```html
<!DOCTYPE html>
<html lang="en">
<head>
<meta charset="utf-8">
<title>Brindlequay – Board Members Banner</title>
<link href="https://fonts.googleapis.com/css2?family=Roboto+Condensed:ital,wght@0,400;0,700;1,700&family=Kaushan+Script&display=swap" rel="stylesheet">
<style>
  :root {
    --navy: #1f2a6b;
    --red: #c8102e;
    --dark-red: #8e0b1f;
    --green: #2f8a3c;
    --paper: #f4f4f2;
    --photo-light: #e9ddd2;
    --photo-mid: #b58a6a;
    --photo-dark: #5a3a2a;
  }
  * { margin: 0; padding: 0; box-sizing: border-box; }
  html, body { width: 681px; height: 1200px; overflow: hidden; background: #ffffff; }
  .banner {
    position: relative;
    width: 681px;
    height: 1200px;
    background: var(--paper);
    font-family: "Roboto Condensed", "Arial Narrow", sans-serif;
    overflow: hidden;
  }
  .hero-photo {
    position: absolute;
    left: 0; top: 0;
    width: 681px; height: 300px;
    background:
      radial-gradient(ellipse at 30% 75%, var(--photo-dark) 0%, var(--photo-mid) 35%, transparent 65%),
      radial-gradient(ellipse at 75% 30%, var(--photo-mid) 0%, transparent 55%),
      linear-gradient(180deg, var(--photo-light) 0%, #f6f1ec 100%);
  }
  .board-badge {
    position: absolute;
    left: 375px; top: 268px;
    width: 290px; height: 130px;
  }
  .board-badge svg { position: absolute; inset: 0; }
  .board-badge span {
    position: absolute; inset: 0;
    display: flex; flex-direction: column; align-items: center; justify-content: center;
    color: #ffffff;
    font-weight: 700; font-size: 34px; line-height: 1;
    letter-spacing: 0.5px;
  }
  .stress-list {
    position: absolute;
    left: 26px; right: 24px; top: 405px;
    font-size: 29.5px;
    line-height: 34px;
    font-weight: 700;
    letter-spacing: -0.2px;
  }
  .stress { color: var(--navy); }
  .relax { color: var(--navy); margin-bottom: 0; }
  .relax-lead { color: var(--red); font-style: italic; font-size: 32px; }
  .tagline {
    font-family: "Kaushan Script", cursive;
    color: var(--green);
    font-weight: 400;
    font-size: 29px;
  }
  .call-to-action {
    position: absolute;
    left: 0; right: 0; top: 1000px;
    text-align: center;
    color: var(--red);
    font-weight: 700; font-style: italic;
    font-size: 32px;
    letter-spacing: 0.3px;
  }
  .brand {
    position: absolute;
    left: 0; right: 0; top: 1072px;
    display: flex; flex-direction: column; align-items: center;
  }
  .brand-row { display: flex; align-items: center; gap: 16px; }
  .brand-mark { width: 46px; height: 46px; background: var(--green); }
  .brand-name {
    color: var(--navy);
    font-weight: 700;
    font-size: 50px;
    line-height: 1;
    letter-spacing: 1px;
  }
  .brand-rule { width: 430px; height: 3px; background: var(--navy); margin: 10px 0 8px; }
  .brand-since { color: var(--navy); font-size: 22px; font-weight: 400; letter-spacing: 3px; }
</style>
</head>
<body>
  <main class="banner">
    <div class="hero-photo" role="img" aria-label="Photo of a woman relaxing face down while receiving a shoulder massage"></div>

    <div class="board-badge">
      <svg viewBox="0 0 290 130" width="290" height="130" aria-hidden="true">
        <polygon points="0,0 290,0 270,22 290,44 270,66 290,88 270,108 290,130 0,130 20,108 0,88 20,66 0,44 20,22" fill="var(--dark-red)"/>
        <polygon points="8,8 282,8 263,26 282,46 263,66 282,86 263,104 282,122 8,122 27,104 8,86 27,66 8,46 27,26" fill="var(--red)"/>
      </svg>
      <span>FOR BOARD<br>MEMBERS</span>
    </div>

    <section class="stress-list">
      <p class="stress">Stress: THE BOARD HAS TOO MUCH WORK TO DO</p>
      <p class="relax"><span class="relax-lead">Relax...</span>and let us do the work.</p>
      <p class="stress">Stress: YOUR COMMUNITY HAS “ISSUES.”</p>
      <p class="relax"><span class="relax-lead">Relax...</span>and let us give you a <span class="tagline">Copper Lantern</span>.</p>
      <p class="stress">Stress: YOUR MEMBERS CANNOT PAY ONLINE.</p>
      <p class="relax"><span class="relax-lead">Relax...</span>we’ll give your members multiple ways to pay.</p>
      <p class="stress">Stress: COMMUNICATION IS POOR OR INCONSISTENT.</p>
      <p class="relax"><span class="relax-lead">Relax...</span>we’ll keep you informed with a robust online portal, chock full of information.</p>
      <p class="stress">Stress: YOUR DELINQUENCIES ARE HIGH.</p>
      <p class="relax"><span class="relax-lead">Relax...</span>as a licensed collection agency, we have developed an effective collections program that works in tandem with your collections attorney. Plus, we can report to the credit bureau!</p>
    </section>

    <p class="call-to-action">COME IN TO TALK AND START RELAXING TODAY!</p>

    <footer class="brand">
      <div class="brand-row">
        <div class="brand-mark"></div>
        <div class="brand-name">BRINDLEQUAY</div>
      </div>
      <div class="brand-rule"></div>
      <div class="brand-since">MANAGEMENT, INC. · SINCE 1987</div>
    </footer>
  </main>
</body>
</html>
```